Military and tactical gear supply company needs web design

We need a web design for a company called U.S. Ravenfield. We provide quality tactical equipment to military and law enforcement. This is an e-commerce business and we primarily market ourselves on social media. Our key products are backpacks, military-style belts, and tactical flashlights. The gear we sell is not yet widely known about, but is on par with the state-of-the-art products in this field. We want the website to convey the message of quality, durability, and reliability. We use the word "kinetic" because the customers in this field are very "action-oriented" and we would like that idea to be communicated in the web site as well. The primary demographic is men in their 20's-30's, so the web site should have a masculine feel to it. Attached is the logo and color scheme.

```html
<!DOCTYPE html>
<html lang="en">
<head>
<meta charset="utf-8">
<title>U.S. Ravenfield — Tactical Equipment</title>
<link href="https://fonts.googleapis.com/css2?family=Oswald:wght@400;500;600;700&family=Roboto:wght@400;500;700&display=swap" rel="stylesheet">
<style>
:root{
  --navy:#142b44;
  --red:#c4202a;
  --ink:#1d1d1d;
  --grey-bg:#efefef;
  --footer:#111418;
  --muted:#9aa0a6;
  --white:#ffffff;
}
*{box-sizing:border-box;margin:0;padding:0}
html,body{width:1200px;height:3556px;overflow:hidden;background:var(--white)}
body{position:relative;font-family:'Roboto',sans-serif;color:var(--ink)}
.abs{position:absolute}
.brand{font-family:'Oswald',sans-serif;font-weight:700;letter-spacing:1px}

/* header */
.topbar{left:0;top:0;width:1200px;height:88px;background:var(--white)}
.topbar .brand{left:80px;top:24px;font-size:30px;color:var(--navy)}
.search{left:388px;top:30px;width:432px;height:32px;border:1px solid #c9c9c9;display:flex}
.search span{flex:1;padding:7px 12px;font-size:13px;color:#999}
.search i{width:36px;background:var(--red);display:flex;align-items:center;justify-content:center}
.cart{left:944px;top:34px}
.account{left:1000px;top:30px;width:112px;height:32px;background:var(--red);color:#fff;font-size:13px;display:flex;align-items:center;justify-content:center;gap:6px}
.nav{left:0;top:88px;width:1200px;height:44px;background:var(--navy)}
.nav a{color:#fff;text-decoration:none;font-size:14px;font-weight:500;position:absolute;top:14px}

/* hero */
.hero{left:0;top:132px;width:1200px;height:548px;background:linear-gradient(160deg,#cfd6dc 0%,#8d979f 30%,#4d555b 65%,#2a2f33 100%)}
.hero-copy{left:160px;top:300px;width:460px;text-align:center;color:#fff}
.hero-copy .brand{font-size:34px;color:#fff;display:block;margin-bottom:26px}
.hero-copy p{font-size:24px;font-weight:400}
.hero-copy h1{font-family:'Oswald',sans-serif;font-size:38px;font-weight:600;margin-top:6px}
.btn-outline{display:inline-block;border:1px solid #fff;color:#fff;font-size:12px;font-weight:500;padding:9px 26px;letter-spacing:.5px}
.hero-copy .btn-outline{margin-top:30px;background:rgba(0,0,0,.2)}

/* partners */
.partners{left:40px;top:750px;width:1120px;height:110px;display:flex;justify-content:space-between;align-items:center}
.partners span{width:90px;height:44px;background:#d7d7d7;border-radius:4px}
.partners span.round{width:70px;height:70px;border-radius:50%}

/* categories */
.categories{left:0;top:900px;width:1200px;height:800px;background:var(--grey-bg)}
.kicker{width:1200px;text-align:center;font-size:24px;color:#333}
.section-title{width:1200px;text-align:center;font-family:'Oswald',sans-serif;font-size:42px;font-weight:600;color:#111}
.tile{overflow:hidden}
.tile .label{position:absolute;left:20px;bottom:20px;color:#fff;font-size:15px;font-weight:700;text-transform:uppercase;letter-spacing:.5px}
.tile .btn-outline{position:absolute;left:110px;top:104px;background:rgba(0,0,0,.35)}

/* featured */
.arrow-btn{width:40px;height:40px;background:#c9c9c9;display:flex;align-items:center;justify-content:center}
.view-all{left:968px;top:1832px;color:var(--red);font-family:'Oswald',sans-serif;font-size:22px;display:flex;gap:8px;align-items:center}
.product{width:228px;text-align:center}
.product .photo{width:228px;height:228px;border:1px solid #bdbdbd;display:flex;align-items:center;justify-content:center;position:relative}
.product .photo div{width:150px;height:170px}
.product h3{font-size:16px;font-weight:400;margin-top:36px;color:#222}
.product .price{font-size:18px;color:var(--red);font-weight:500;margin-top:14px}
.btn-red-outline{display:inline-block;border:1px solid var(--red);color:var(--red);font-size:12px;padding:8px 18px;margin-top:18px}

/* promo */
.promo{left:0;top:2380px;width:1200px;height:580px;background:linear-gradient(180deg,#e9edf0 0%,#c7ced3 40%,#5c6166 75%,#2a2b2d 100%)}
.promo-copy{left:636px;color:#fff}
.promo-copy h2{font-family:'Oswald',sans-serif;font-size:58px;font-weight:500;color:#2b2b2b;letter-spacing:1px}
.promo-copy .deal{font-family:'Oswald',sans-serif;color:#fff;font-size:42px;font-weight:300;margin-top:-4px}
.promo-copy .deal b{font-size:96px;font-weight:700}
.promo-copy .btn-outline{margin-left:68px;margin-top:14px;background:rgba(0,0,0,.3)}

/* footer */
.footer{left:0;top:2960px;width:1200px;height:596px;background:var(--footer);color:#d6d6d6}
.footer .brand{left:168px;top:104px;font-size:34px;color:#fff}
.footer .about{left:168px;top:200px;width:280px;font-size:13px;line-height:20px;color:#cfcfcf}
.social{left:172px;top:364px;display:flex;gap:26px}
.social span{width:22px;height:22px;border-radius:50%;background:#e4e4e4}
.news-title{left:540px;top:92px;font-size:14px;font-weight:500;color:#fff;letter-spacing:.5px}
.news-input{left:540px;top:116px;width:336px;height:36px;background:#fff;color:#888;font-size:13px;padding:10px 14px}
.news-btn{left:900px;top:116px;width:128px;height:36px;background:var(--red);color:#fff;font-size:12px;font-weight:500;display:flex;align-items:center;justify-content:center;letter-spacing:.5px}
.links{top:224px;list-style:none;font-size:13px;line-height:29px;color:#e0e0e0}
.copyline{left:0;top:3480px;width:1200px;border-top:1px solid #2c3036}
.copyright{left:184px;top:3512px;font-size:13px;color:#cfcfcf}
</style>
</head>
<body>

<header class="abs topbar">
  <div class="abs brand">U.S. Ravenfield</div>
  <div class="abs search"><span>Search Here</span><i><svg width="16" height="16" viewBox="0 0 16 16"><circle cx="7" cy="7" r="5" fill="none" stroke="#fff" stroke-width="2"/><line x1="10.5" y1="10.5" x2="14" y2="14" stroke="#fff" stroke-width="2"/></svg></i></div>
  <svg class="abs cart" width="24" height="22" viewBox="0 0 24 22"><path d="M1 2h4l3 12h12l3-9H7" fill="none" stroke="#222" stroke-width="2"/><circle cx="10" cy="19" r="2" fill="#222"/><circle cx="18" cy="19" r="2" fill="#222"/></svg>
  <div class="abs account"><svg width="12" height="12" viewBox="0 0 12 12"><circle cx="6" cy="4" r="3" fill="#fff"/><path d="M0 12c0-4 12-4 12 0z" fill="#fff"/></svg>My Account</div>
</header>

<nav class="abs nav">
  <a style="left:120px">Categories ▾</a>
  <a style="left:250px">Footwear</a>
  <a style="left:370px">Equipments ▾</a>
  <a style="left:510px">Backpacks</a>
  <a style="left:640px">Featured Items ▾</a>
  <a style="left:806px">Orders</a>
  <a style="left:912px">Track ▾</a>
  <a style="left:1024px">Contact</a>
</nav>

<section class="abs hero" role="img" aria-label="Soldier in hooded jacket with backpack facing snowy mountains"></section>
<div class="abs hero-copy">
  <span class="brand">U.S. Ravenfield</span>
  <p>We Provide Quality Tactical Equipment to</p>
  <h1>Military and Law Enforcement</h1>
  <span class="btn-outline">SHOP NOW</span>
</div>

<div class="abs partners" aria-label="Partner brands">
  <span class="round"></span><span></span><span class="round"></span><span></span><span class="round"></span><span class="round"></span><span></span><span class="round"></span><span></span>
</div>

<section class="abs categories"></section>
<p class="abs kicker" style="left:0;top:946px">Buy our products</p>
<h2 class="abs section-title" style="left:0;top:976px">Shop By Categories</h2>

<div class="abs tile" style="left:40px;top:1048px;width:360px;height:244px;background:linear-gradient(135deg,#3a3a3a,#151515)" role="img" aria-label="Military boots on a dark background"><span class="label">Military Boots</span></div>
<div class="abs tile" style="left:40px;top:1316px;width:360px;height:252px;background:linear-gradient(135deg,#4a4d50,#1d1f21)" role="img" aria-label="Tactical flashlight in hand"><span class="btn-outline">SHOP NOW</span><span class="label">Tactical Flashlight</span></div>
<div class="abs tile" style="left:420px;top:1088px;width:360px;height:480px;background:linear-gradient(180deg,#8b8680,#3d5a66 55%,#5c4d40)" role="img" aria-label="Climber carrying a large teal backpack"><span class="label">Backpacks</span></div>
<div class="abs tile" style="left:800px;top:1048px;width:360px;height:244px;background:linear-gradient(135deg,#5a5a5a,#1e1e1e)" role="img" aria-label="Black military style belt with buckle"><span class="label">Military Style Belts</span></div>
<div class="abs tile" style="left:800px;top:1316px;width:360px;height:252px;background:linear-gradient(135deg,#e8e8e8,#b9b2ad 60%,#6b3f2a)" role="img" aria-label="Pair of brown leather gloves"><span class="label">Tactical Gloves</span></div>

<p class="abs kicker" style="left:0;top:1784px">Best deal products</p>
<h2 class="abs section-title" style="left:0;top:1814px">Featured Products</h2>
<div class="abs arrow-btn" style="left:120px;top:1816px"><svg width="14" height="14" viewBox="0 0 14 14"><path d="M9 2L4 7l5 5" fill="none" stroke="#fff" stroke-width="2"/></svg></div>
<div class="abs arrow-btn" style="left:172px;top:1816px"><svg width="14" height="14" viewBox="0 0 14 14"><path d="M5 2l5 5-5 5" fill="none" stroke="#fff" stroke-width="2"/></svg></div>
<div class="abs view-all">View All <svg width="18" height="14" viewBox="0 0 18 14"><path d="M0 7h16M10 1l6 6-6 6" fill="none" stroke="#c4202a" stroke-width="2"/></svg></div>

<article class="abs product" style="left:72px;top:1912px">
  <div class="photo"><div role="img" aria-label="Army green canvas backpack" style="background:linear-gradient(180deg,#5d5a42,#3c3a2c)"></div></div>
  <h3>Army green backpack</h3><p class="price">$64.00</p>
</article>
<article class="abs product" style="left:348px;top:1912px">
  <div class="photo"><div role="img" aria-label="Black tactical flashlight" style="height:50px;background:linear-gradient(90deg,#111,#444)"></div></div>
  <h3>Tactic Flashlight 1</h3><p class="price">$57.00</p>
</article>
<article class="abs product" style="left:620px;top:1912px">
  <div class="photo"><div role="img" aria-label="Coiled black military belt" style="height:110px;border-radius:50%;background:radial-gradient(circle,#fff 30%,#222 32%,#333 60%,#fff 62%)"></div>
    <svg style="position:absolute;left:14px;bottom:12px" width="16" height="14" viewBox="0 0 24 22"><path d="M1 2h4l3 12h12l3-9H7" fill="none" stroke="#222" stroke-width="2.5"/></svg>
    <svg style="position:absolute;right:14px;bottom:12px" width="14" height="14" viewBox="0 0 14 14"><path d="M1 5V1h4M9 1h4v4M13 9v4H9M5 13H1V9" fill="none" stroke="#222" stroke-width="1.5"/></svg>
  </div>
  <h3>Military Stylish - Belt</h3><p class="price">$44.00</p>
  <span class="btn-red-outline">SHOP NOW</span>
</article>
<article class="abs product" style="left:892px;top:1912px">
  <div class="photo"><div role="img" aria-label="Pair of brown combat boots" style="background:linear-gradient(180deg,#3b3128,#1f1a15)"></div></div>
  <h3>Army Camp - Boot</h3><p class="price">$62.00</p>
</article>

<section class="abs promo" role="img" aria-label="Hiker with yellow jacket and backpack climbing dark rocks"></section>
<div class="abs promo-copy" style="top:2504px">
  <h2>BACKPACKS</h2>
  <p class="deal">Flat <b>20%</b> OFF</p>
  <span class="btn-outline">SHOP NOW</span>
</div>

<footer class="abs footer">
  <div class="abs brand">U.S. Ravenfield</div>
  <p class="abs about">U.S. Ravenfield builds field-ready gear for people who move fast and carry heavy. Every pack, belt and light is tested hard so it holds up when the mission counts most.</p>
  <div class="abs social" aria-label="Social links"><span></span><span></span><span></span><span></span></div>
  <p class="abs news-title">JOIN OUR NEWS LETTER</p>
  <div class="abs news-input">Enter your Email</div>
  <div class="abs news-btn">SUBSCRIBE</div>
  <ul class="abs links" style="left:512px"><li>My Account</li><li>Contact Us</li><li>Ravenfield Rewards</li><li>Request Quote</li><li>Bulk Order Info</li><li>Promotions</li><li>Why Buy From Us?</li></ul>
  <ul class="abs links" style="left:720px"><li>Home</li><li>About Us</li><li>Contact</li><li>Terms &amp; Condition</li><li>Privacy Policy</li><li>Copyrights</li><li>New Arrivals</li></ul>
  <ul class="abs links" style="left:940px"><li>Bulk Order Info</li><li>Promotions</li><li>Why Buy From Us?</li><li>My Account</li><li>Contact Us</li><li>Ravenfield Rewards</li><li>Request Quote</li></ul>
</footer>
<div class="abs copyline"></div>
<p class="abs copyright">© 2020 U.S. Ravenfield. All rights reserved.</p>

</body>
</html>
```